Building company business card

Design and print business cards for BREVOTA PTY LTD.
A residantial homes building company.
Pixel Forge already designed the company Logo.

```html
<!DOCTYPE html>
<html lang="en">
<head>
<meta charset="utf-8">
<title>BREVOTA PTY LTD – Business Card</title>
<link rel="stylesheet" href="https://fonts.googleapis.com/css2?family=Oswald:wght@700&family=Arimo:wght@400&display=swap">
<style>
  :root {
    --page-bg: #e6e2db;
    --navy-deep: #18205e;
    --navy-mid: #2c3790;
    --navy-light: #3b48a6;
    --gold: #d79a2b;
    --gold-soft: #e2a93c;
    --frost-light: #f3ece0;
    --frost-dark: #d8cfbf;
    --text-light: #e9e8f2;
  }
  * { margin: 0; padding: 0; box-sizing: border-box; }
  html, body {
    width: 1200px; height: 897px; overflow: hidden;
    background: var(--page-bg);
  }
  .card {
    position: absolute; left: 50px; top: 150px;
    width: 1100px; height: 598px;
    border-radius: 26px; overflow: hidden;
    background: linear-gradient(160deg, var(--frost-light), var(--frost-dark));
    box-shadow: 0 10px 30px rgba(0,0,0,0.18);
    font-family: "Arimo", Arial, sans-serif;
  }
  .card-shapes { position: absolute; inset: 0; }
  .name-tab {
    position: absolute; left: 0; top: 72px; width: 18px; height: 60px;
    background: var(--gold); border-radius: 0 4px 4px 0;
  }
  .holder-name {
    position: absolute; left: 48px; top: 66px;
    font-family: "Oswald", "Arial Narrow", sans-serif; font-weight: 700;
    font-size: 35px; line-height: 1; color: var(--gold-soft); letter-spacing: -0.5px;
  }
  .holder-role {
    position: absolute; left: 49px; top: 112px;
    font-size: 27px; color: var(--text-light);
  }
  .address {
    position: absolute; left: 48px; top: 210px;
    font-size: 25px; line-height: 33px; color: var(--text-light);
  }
  .licence { color: var(--gold-soft); display: block; margin-top: 7px; }
  .contacts {
    position: absolute; left: 44px; top: 382px; list-style: none;
  }
  .contacts li {
    display: flex; align-items: center; height: 37px;
    font-size: 25px; color: var(--text-light);
  }
  .contact-icon { width: 27px; height: 27px; margin-right: 11px; flex: none; }
  .brand-name {
    position: absolute; left: 640px; top: 400px; width: 440px;
    text-align: center;
    font-family: "Arimo", Arial, sans-serif; font-weight: 400;
    font-size: 64px; line-height: 1; color: var(--navy-deep);
  }
</style>
</head>
<body>
  <article class="card">
    <svg class="card-shapes" viewBox="0 0 1100 598" width="1100" height="598" aria-hidden="true">
      <defs>
        <radialGradient id="navyFill" cx="0.35" cy="0.45" r="0.7">
          <stop offset="0" stop-color="#3b48a6"/>
          <stop offset="0.55" stop-color="#2c3790"/>
          <stop offset="1" stop-color="#18205e"/>
        </radialGradient>
      </defs>
      <path class="gold-sweep" fill="#d79a2b" d="M0 0 H688 C578 100 502 228 535 330 C566 440 640 530 700 598 H0Z"/>
      <path class="navy-panel" fill="url(#navyFill)" d="M0 0 H675 C560 100 484 230 515 330 C545 440 610 530 665 598 H0Z"/>
    </svg>

    <div class="name-tab"></div>
    <h1 class="holder-name">DORIAN (Dee) KASSOS</h1>
    <p class="holder-role">Director</p>

    <p class="address">PO Box 482<br>Ferndale Vic 3190<span class="licence">CDB-U 51846</span></p>

    <ul class="contacts">
      <li>
        <svg class="contact-icon" viewBox="0 0 28 28"><circle cx="14" cy="14" r="14" fill="#d79a2b"/><rect x="10" y="7" width="8" height="14" rx="1.5" fill="none" stroke="#fff" stroke-width="1.8"/><circle cx="14" cy="18.5" r="0.9" fill="#fff"/></svg>
        0412 555 308
      </li>
      <li>
        <svg class="contact-icon" viewBox="0 0 28 28"><circle cx="14" cy="14" r="14" fill="#d79a2b"/><path d="M9 8 l3 -1 2 4 -2 1.5 c1 2 2.5 3.5 4.5 4.5 l1.5 -2 4 2 -1 3 c-6 0 -12 -6 -12 -12z" fill="#fff"/></svg>
        0433 555 162
      </li>
      <li>
        <svg class="contact-icon" viewBox="0 0 28 28"><circle cx="14" cy="14" r="14" fill="#d79a2b"/><rect x="7" y="9" width="14" height="10" rx="1" fill="#fff"/><path d="M7.5 9.5 L14 15 L20.5 9.5" fill="none" stroke="#d79a2b" stroke-width="1.5"/></svg>
        dk@brevota-pl.com
      </li>
      <li>
        <svg class="contact-icon" viewBox="0 0 28 28"><circle cx="14" cy="14" r="14" fill="#d79a2b"/><circle cx="14" cy="14" r="7" fill="none" stroke="#fff" stroke-width="1.6"/><path d="M7 14 H21 M14 7 C10 10 10 18 14 21 M14 7 C18 10 18 18 14 21" fill="none" stroke="#fff" stroke-width="1.3"/></svg>
        www.brevota-pl.com
      </li>
    </ul>

    <p class="brand-name">BREVOTA</p>
  </article>
</body>
</html>
```